A start-up to help youth sports programs needs a designed 4-Page PDF.

We need a 4-page PDF that will be included with an email to coaches and parents to give them an overview of our Brightfield Crew program, and their steps to get started.

We have just finished the webpage for the initiative - www.brightfield-crew.org.

We will use our RWT logo (not the www.RWTHoopcamp.com logo), as this program is for every sport. We have not created a Brightfield Crew logo as of yet, but would like one. The RWT logo should be small and not prominent, but the title Brightfield Crew should be large on the first page.

We would like to use our RWT colors of orange, black, gray and blue.

The design should not have images, clipart or graphics showing lots of sports. We just need something clean and professional.

Here is the doc with all the content, including the introductory emails (no action is needed on the emails) - https://files.example-docshare.net/doc/7QwLm3xRtY9zPa2VbNc8KdJ4sHfE6uG1oTiX5yZr/view

Font styles to use
Sans Serif

```html
<!DOCTYPE html>
<html lang="en">
<head>
<meta charset="utf-8">
<title>Brightfield Crew – Program Overview</title>
<link rel="stylesheet" href="https://fonts.googleapis.com/css2?family=Poppins:wght@500;600;700&family=Montserrat:wght@400;600;700&display=swap">
<style>
  :root{
    --canvas:#ffffff;
    --page:#e9eaec;
    --ink:#111111;
    --navy:#1f2a44;
    --panel:#000000;
    --panel-text:#ffffff;
    --photo-a:#6d6d6d;
    --photo-b:#2b2b2b;
  }
  *{margin:0;padding:0;box-sizing:border-box}
  html,body{width:848px;height:1200px;overflow:hidden;background:var(--canvas)}
  body{position:relative;font-family:"Montserrat",sans-serif;color:var(--ink)}
  .page{position:absolute;width:307px;height:434px;background:var(--page);overflow:hidden}
  .page--intro{left:76px;top:130px}
  .page--parents{left:477px;top:130px}
  .page--coaches{left:76px;top:652px}
  .page--fundamentals{left:477px;top:652px}
  .abs{position:absolute}
  .brand{position:absolute;display:flex;align-items:center;gap:3px;font-family:"Poppins",sans-serif;font-weight:700;color:var(--ink);letter-spacing:.5px}
  .brand__dot{border-radius:50%;background:var(--ink)}
  .display{font-family:"Poppins",sans-serif;font-weight:600;text-transform:uppercase;color:var(--ink)}
  .rule{position:absolute;height:1px;background:var(--ink)}
  .lead{font-family:"Poppins",sans-serif;font-weight:600}
  .small{font-size:5.3px;line-height:7.1px}
  .footer{position:absolute;right:15px;top:416px;font-size:6px}
  .step-title{font-family:"Poppins",sans-serif;font-weight:700;color:var(--navy);line-height:1.05;letter-spacing:-.2px}
  .panel{position:absolute;background:var(--panel);color:var(--panel-text)}
  ul.bullets{list-style:disc;padding-left:6px}
  ul.plain{list-style:disc;padding-left:7px;font-size:6px;line-height:7.75px}
  ol.ideas{padding-left:10px}
  .section-head{font-family:"Montserrat",sans-serif;font-weight:500;font-size:10.5px;letter-spacing:.2px}
</style>
</head>
<body>

<!-- Page 1: introduction -->
<section class="page page--intro">
  <div class="brand" style="left:219px;top:21px;font-size:18px"><span class="brand__dot" style="width:12px;height:12px"></span>RWT</div>
  <h1 class="display abs" style="left:16px;top:48px;font-size:34px;line-height:38px">Brightfield<br>Crew</h1>
  <div class="abs" style="left:16px;top:125px;width:46px;height:2px;background:var(--ink)"></div>
  <p class="lead abs" style="left:16px;top:134px;font-size:7.4px;line-height:10px">Giving Athletes the Experience<br>They Deserve</p>
  <p class="abs small" style="left:16px;top:162px;width:112px">Brightfield Crew has been designed to raise standards, reduce frustrations, and give teams the ultimate edge.</p>
  <h2 class="display abs" style="left:16px;top:186px;font-size:14px;line-height:21.5px;font-weight:500">Our<br>“Fundamentals”<br>Help…</h2>
  <h2 class="display abs" style="right:15px;top:182px;font-size:14px;line-height:21.5px;font-weight:500;text-align:right">We know<br>your time is<br>limited…</h2>
  <div class="rule" style="left:16px;width:276px;top:255px"></div>
  <ul class="bullets abs small" style="left:20px;top:264px;width:104px">
    <li><b>Coaches</b> understand the Fundamentals of being a great coach.</li>
    <li><b>Parents</b> discover the Fundamentals of being a supportive sports parent.</li>
    <li><b>Players</b> learn the Fundamentals of being a great athlete, teammate, and leader</li>
  </ul>
  <p class="abs small" style="left:188px;top:264px;width:106px">Which is why our simple-to-apply Fundamentals videos are only a few minutes long. And in nearly no time, everyone will have a common language to use and clear expectations to uphold.</p>
  <h2 class="display abs" style="left:20px;top:335px;font-size:12.5px;font-weight:500">The Real Magic…</h2>
  <p class="abs small" style="left:20px;top:355px;width:268px">Beyond the initial viewing of the videos, the real magic is the weekly reinforcement and top-of-mind awareness of the Fundamentals — in real time during the season.</p>
  <p class="abs small" style="left:20px;top:374px">Better Coaches + Better Players + Better Parents<br>= <b>A Better Sports Experience</b></p>
  <div class="rule" style="left:16px;width:276px;top:396px"></div>
  <p class="footer">Brightfield-Crew.org</p>
</section>

<!-- Page 2: parents -->
<section class="page page--parents">
  <div class="brand" style="left:219px;top:21px;font-size:18px"><span class="brand__dot" style="width:12px;height:12px"></span>RWT</div>
  <h1 class="display abs" style="left:17px;top:48px;font-size:38px;line-height:39px">Next<br>Steps for<br>Parents…</h1>
  <div class="rule" style="left:12px;width:276px;top:189px"></div>
  <h3 class="step-title abs" style="left:21px;top:209px;width:118px;font-size:9.4px">Step 1 - Watch the Initial Parent Fundamentals Course</h3>
  <p class="abs" style="left:21px;top:249px;width:118px;font-size:6.1px;line-height:7.8px">Complete the 45-minute course and sign the code of conduct within the next 10 days.</p>
  <p class="abs" style="left:21px;top:280px;width:112px;font-size:6.1px;line-height:7.8px">You will also have access to the Coach and Player Fundamentals courses.</p>
  <h3 class="step-title abs" style="left:180px;top:250px;width:110px;font-size:10.4px">Step 2 - Watch the Weekly Videos</h3>
  <p class="abs" style="left:190px;top:280px;width:108px;font-size:5px;line-height:7.1px">Each Sunday, you will be emailed a weekly Parent Fundamentals video that reinforces one of the 10 Parent Fundamentals. Total time - 3-5 minutes</p>
  <p class="abs" style="left:190px;top:316px;width:108px;font-size:5px;line-height:7.1px">You will also receive two Player Fundamental videos for the week to watch with your child. At practice, the coach will take a few minutes to discuss how the players can apply these Fundamentals in the season.</p>
  <div class="rule" style="left:16px;width:276px;top:396px"></div>
  <p class="footer">Brightfield-Crew.org</p>
</section>

<!-- Page 3: coaches -->
<section class="page page--coaches">
  <div class="brand" style="left:14px;top:70px;font-size:19px"><span class="brand__dot" style="width:14px;height:14px"></span>RWT</div>
  <h1 class="display abs" style="left:169px;top:18px;font-size:22px;line-height:22px">Next<br>Steps for<br>Coaches</h1>
  <p class="display abs" style="left:169px;top:92px;font-size:14px;font-weight:700">…</p>
  <h3 class="step-title abs" style="left:169px;top:114px;width:100px;font-size:10.2px">Step 1 - Watch the Initial Coach Fundamentals Course</h3>
  <p class="abs" style="left:169px;top:161px;width:110px;font-size:5px;line-height:6.9px">Complete the 45-minute course and sign the code of conduct within the next 10 days. You will also have access to the Parent and Player Fundamentals courses to watch any time.</p>
  <h3 class="step-title abs" style="left:169px;top:208px;width:100px;font-size:10.2px">Step 3 - Watch the Weekly Videos for You and Your Team</h3>
  <p class="abs" style="left:170px;top:256px;width:112px;font-size:5px;line-height:6.9px">Each Sunday, you will be emailed a Coach Fundamental video to watch to deepen your understanding of the topic. Total time - 3-5 minutes</p>
  <p class="abs" style="left:170px;top:291px;width:112px;font-size:5px;line-height:6.9px">You will also receive two Player Fundamental videos for the week to show your team. Be sure to take a few minutes to celebrate players who are living out the Fundamentals of the week and to discuss how the team can further apply them.</p>
  <p class="abs" style="left:174px;top:346px;font-size:4.6px;font-weight:700">Can’t Show the Videos at Practice?</p>
  <p class="abs" style="left:174px;top:358px;width:106px;font-size:4.3px;line-height:6.1px">If you don’t have a suitable, quiet space to watch the video as a team, request that your parents play the videos for their son or daughter on the drive to practice, as the weekly videos will be emailed to parents and players as well.</p>
  <div class="panel" style="left:14px;top:151px;width:123px;height:197px">
    <h3 class="abs" style="left:8px;top:9px;width:110px;font-family:'Poppins',sans-serif;font-weight:700;font-size:10.4px;line-height:11px">Step 2 - Show Your Team the Player Fundamentals Course</h3>
    <p class="abs" style="left:8px;top:65px;width:110px;font-size:5px;line-height:7px">Introduce the players to the 16 Player Fundamentals as early in the season as possible. Time required - 60 minutes (The course includes videos &amp; discussion questions.)</p>
    <p class="abs" style="left:13px;top:105px;width:104px;font-size:4.3px;line-height:6px"><b>Ideas For Showing the Course:</b> (depending on time and availability of a quiet space &amp; wifi):</p>
    <ol class="ideas abs" style="left:13px;top:123px;width:104px;font-size:4.3px;line-height:6px">
      <li>Have a special team retreat pizza night and go through the course.</li>
      <li>Show 4 Fundamental videos before or after your next 4 practices. (15 min each)</li>
      <li>Show the course between games at an early season tournament/event</li>
    </ol>
  </div>
  <p class="footer">Brightfield-Crew.org</p>
</section>

<!-- Page 4: fundamentals list -->
<section class="page page--fundamentals">
  <div class="brand" style="left:248px;top:9px;font-size:13px"><span class="brand__dot" style="width:9px;height:9px"></span>RWT</div>
  <p class="lead abs" style="left:13px;top:31px;font-size:7.3px;line-height:10px">I realized it will be helpful to have this 4th (and if needed<br>5th) page of content, so please include it in your design.</p>
  <h2 class="section-head abs" style="left:13px;top:58px">COACH FUNDAMENTALS</h2>
  <ul class="plain abs" style="left:23px;top:72px">
    <li>Be Professional</li><li>Create a Safe Space</li><li>Enroll Parents</li><li>Connect Before You Correct</li><li>Set High Standards</li><li>Hold Others Accountable</li><li>Run Effective Practices</li><li>Focus on the Process</li><li>Foster Teamwork</li><li>Instill Confidence</li><li>Develop Winners</li><li>Respect Officials</li>
  </ul>
  <h2 class="section-head abs" style="left:13px;top:172px">PARENT FUNDAMENTALS</h2>
  <ul class="plain abs" style="left:28px;top:186px">
    <li>Be a Safe Space</li><li>Let Go</li><li>Foster Resilience</li><li>Make a Contribution</li><li>Protect Their Identity</li><li>Respect Officials</li><li>Strengthen Bonds</li><li>Honor Boundaries</li><li>Support the Coach</li><li>Drop Your Fears</li>
  </ul>
  <h2 class="section-head abs" style="left:13px;top:271px">PLAYER FUNDAMENTALS</h2>
  <ul class="plain abs" style="left:28px;top:285px">
    <li>Be Coachable</li><li>Be Grateful</li><li>Be Precise</li><li>Be the Best You</li><li>Be Unruffleable</li><li>Beat You-Yesterday</li><li>Hustle as a Habit</li><li>Light Up Others</li><li>Lock In</li><li>Protect Your Confidence</li><li>Take Care of Your Body</li><li>Take Ultra Ownership</li><li>Think Like a Captain</li><li>Welcome Adversity</li><li>Be a Team Player</li><li>Be Consistent</li>
  </ul>
  <aside class="panel" style="left:174px;top:96px;width:124px;height:274px">
    <div role="img" aria-label="Portrait photo of the instructor" class="abs" style="left:74px;top:8px;width:42px;height:60px;background:linear-gradient(160deg,var(--photo-a),var(--photo-b))"></div>
    <h3 class="abs" style="left:8px;top:40px;font-family:'Poppins',sans-serif;font-weight:700;font-size:7px;line-height:10px">Meet Your<br>Instructor<br>Dario Keller</h3>
    <p class="abs" style="left:8px;top:81px;width:110px;font-size:6px;line-height:7.7px">Dario is the President of RWT, the leading education program in the world for teaching basketball players how to think the game, lead their team, and develop a winning mindset.<br><br>RWT impacts over 20,000 players and coaches each summer through 200+ camps across North America. Over 175,000 athletes and 15,000 coaches have attended RWT over the past 32 years.<br><br>As a coach, Dario has led teams at nearly every level of play, from youth sports to high school sports to college teams. Dario is a highly sought-after speaker who has inspired over 250,000 students and educators around the world, and reaches hundreds of thousands online each year.</p>
  </aside>
  <p class="footer">Brightfield-Crew.org</p>
</section>

</body>
</html>
```